6 Banners for $150,000 Media Campaign in Sydney

Please design a series of call to action banners to advertise this campaign and encourage people to join the CHIROPRACTIC CAMPAIGN

https://www.fundorvale.example/projects/sydney-spinewell-drive-2015

banner must rotate with 3 screens and not be longer than 30 seconds in total and less than 45kb

The call to action must be "Join The Campaign"

These are the sizes:
160x600.gif
728x90.gif
300x250.gif
320x50.gif
300x600.gif

600x315.jpeg (and text can only be 20% of image area - https://www.plimora.example/ads/tools/text_overlay)

FRAME 1:
12 WEEK Chiropractic Campaign (Sydney)
Start June 2015

FRAME 2:
"KEEP YOUR BACK HAPPY"

FRAME 3:
Strictly limited to 300 members

CALL TO ACTION:
JOIN NOW

Target Market(s)

business owners: chiropractors

Industry/Entity Type

Media

Font styles to use
Sans Serif

Requirements
Must have
• strong call to action
• please present ALL banners in a SINGLE file / image

```html
<!DOCTYPE html>
<html lang="en">
<head>
<meta charset="utf-8">
<title>12 Week Chiropractic Campaign – Banner Set</title>
<link rel="stylesheet" href="https://fonts.googleapis.com/css2?family=Montserrat:wght@300;400;700&display=swap">
<style>
  :root {
    --brand-blue: #3498cd;
    --brand-blue-deep: #1d4f73;
    --map-blue: #14aef0;
    --map-blue-dark: #0b7fcf;
    --figure-dark: #1c4f78;
    --figure-light: #4fb3e3;
    --paper: #ffffff;
    --shadow: rgba(60, 60, 70, 0.35);
    --button-top: #0d6b99;
    --button-bottom: #03334f;
    --glow: #29f0ff;
  }
  html, body {
    margin: 0;
    padding: 0;
    width: 1200px;
    height: 1000px;
    overflow: hidden;
    background: var(--paper);
  }
  .banner-sheet {
    position: relative;
    width: 1200px;
    height: 1000px;
    font-family: "Montserrat", Arial, sans-serif;
  }
  .banner {
    position: absolute;
    display: block;
    background: var(--paper);
    box-shadow: 6px 6px 5px var(--shadow);
  }
  .banner svg { display: block; }
  .headline { font-weight: 300; fill: var(--paper); letter-spacing: 0.5px; }
  .subline { font-weight: 300; fill: var(--paper); }
  .tagline { font-weight: 300; fill: var(--brand-blue); letter-spacing: 0.5px; }
  .tagline-strong { fill: var(--brand-blue-deep); }
  .place-label { font-weight: 700; fill: var(--paper); }
  .band { fill: var(--brand-blue); }
  .cta-label { font-weight: 300; fill: var(--paper); letter-spacing: 1px; }

  .banner--skyscraper { left: 132px; top: 64px; width: 160px; height: 600px; }
  .banner--rectangle  { left: 373px; top: 64px; width: 300px; height: 250px; }
  .banner--half-page  { left: 736px; top: 58px; width: 300px; height: 600px; }
  .banner--mobile     { left: 363px; top: 475px; width: 320px; height: 50px; }
  .banner--leaderboard{ left: 186px; top: 687px; width: 728px; height: 90px; }
</style>
</head>
<body>
<main class="banner-sheet">

  <svg width="0" height="0" aria-hidden="true" style="position:absolute">
    <defs>
      <linearGradient id="figure-fill" x1="0" y1="0" x2="0" y2="1">
        <stop offset="0" stop-color="var(--figure-dark)"/>
        <stop offset="0.5" stop-color="var(--figure-light)"/>
        <stop offset="1" stop-color="var(--figure-dark)"/>
      </linearGradient>
      <linearGradient id="map-fill" x1="0" y1="0" x2="1" y2="1">
        <stop offset="0" stop-color="var(--map-blue)"/>
        <stop offset="1" stop-color="var(--map-blue-dark)"/>
      </linearGradient>
      <linearGradient id="button-fill" x1="0" y1="0" x2="0" y2="1">
        <stop offset="0" stop-color="var(--button-top)"/>
        <stop offset="1" stop-color="var(--button-bottom)"/>
      </linearGradient>
      <filter id="button-glow" x="-30%" y="-60%" width="160%" height="220%">
        <feGaussianBlur stdDeviation="5"/>
      </filter>
    </defs>
  </svg>

  <!-- 160x600 -->
  <div class="banner banner--skyscraper">
    <svg width="160" height="600" viewBox="0 0 160 600">
      <polygon class="band" points="0,0 160,0 160,148 0,186"/>
      <text class="headline" x="80" y="65" text-anchor="middle" font-size="33">12 WEEK</text>
      <text class="subline" x="80" y="105" text-anchor="middle" font-size="23">Chiropractic</text>
      <text class="subline" x="80" y="135" text-anchor="middle" font-size="23">Campaign</text>
      <rect x="8" y="190" width="144" height="132" rx="14" fill="url(#map-fill)" role="img" aria-label="Map of Australia marking Sydney"/>
      <text class="place-label" x="72" y="256" text-anchor="middle" font-size="22">Sydney</text>
      <polygon class="band" points="0,362 160,324 160,600 0,600"/>
      <rect x="0" y="330" width="160" height="270" fill="url(#figure-fill)" opacity="0.85" role="img" aria-label="Illustration of a spine and skeleton, back view, hand on neck"/>
    </svg>
  </div>

  <!-- 300x250 -->
  <div class="banner banner--rectangle">
    <svg width="300" height="250" viewBox="0 0 300 250">
      <polygon class="band" points="0,0 300,0 300,64 0,117"/>
      <text class="headline" x="12" y="50" font-size="30">12 WEEK</text>
      <text class="subline" x="290" y="33" text-anchor="end" font-size="20">Chiropractic</text>
      <text class="subline" x="282" y="59" text-anchor="end" font-size="20">Campaign</text>
      <polygon class="band" points="0,222 300,158 300,250 0,250"/>
      <rect x="34" y="108" width="98" height="88" rx="10" fill="url(#map-fill)" role="img" aria-label="Map of Australia marking Sydney"/>
      <text class="place-label" x="82" y="154" text-anchor="middle" font-size="17">Sydney</text>
      <rect x="170" y="82" width="130" height="168" fill="url(#figure-fill)" opacity="0.85" role="img" aria-label="Illustration of a spine and skeleton, back view, hand on neck"/>
    </svg>
  </div>

  <!-- 300x600 -->
  <div class="banner banner--half-page">
    <svg width="300" height="600" viewBox="0 0 300 600">
      <polygon class="band" points="0,0 300,0 300,114 0,186"/>
      <text class="headline" x="134" y="51" text-anchor="middle" font-size="33">12 WEEK</text>
      <text class="subline" x="134" y="92" text-anchor="middle" font-size="23">Chiropractic</text>
      <text class="subline" x="134" y="122" text-anchor="middle" font-size="23">Campaign</text>
      <text class="tagline" x="143" y="187" text-anchor="middle" font-size="23">Strictly</text>
      <text class="tagline" x="143" y="217" text-anchor="middle" font-size="23">Limited To <tspan class="tagline-strong">300</tspan></text>
      <text class="tagline" x="143" y="247" text-anchor="middle" font-size="23">Members</text>
      <rect x="62" y="266" width="160" height="36" fill="var(--glow)" filter="url(#button-glow)" opacity="0.8"/>
      <rect x="62" y="266" width="160" height="36" fill="url(#button-fill)"/>
      <text class="cta-label" x="142" y="290" text-anchor="middle" font-size="16">JOIN NOW</text>
      <polygon class="band" points="0,362 300,290 300,600 0,600"/>
      <rect x="70" y="330" width="200" height="270" fill="url(#figure-fill)" opacity="0.85" role="img" aria-label="Illustration of a spine and skeleton, back view, hand on neck"/>
    </svg>
  </div>

  <!-- 320x50 -->
  <div class="banner banner--mobile">
    <svg width="320" height="50" viewBox="0 0 320 50">
      <polygon class="band" points="0,0 138,0 78,50 0,50"/>
      <text class="headline" x="8" y="19" font-size="17">12 WEEK</text>
      <text class="subline" x="8" y="32" font-size="11">Chiropractic</text>
      <text class="subline" x="8" y="45" font-size="11">Campaign</text>
      <rect x="141" y="3" width="50" height="44" rx="6" fill="url(#map-fill)" role="img" aria-label="Map of Australia marking Sydney"/>
      <text class="place-label" x="165" y="28" text-anchor="middle" font-size="10">Sydney</text>
      <polygon class="band" points="248,0 320,0 320,50 196,50"/>
      <rect x="245" y="2" width="55" height="48" fill="url(#figure-fill)" opacity="0.85" role="img" aria-label="Illustration of a spine and skeleton, back view"/>
    </svg>
  </div>

  <!-- 728x90 -->
  <div class="banner banner--leaderboard">
    <svg width="728" height="90" viewBox="0 0 728 90">
      <polygon class="band" points="0,0 210,0 140,90 0,90"/>
      <text class="headline" x="16" y="36" font-size="29">12 WEEK</text>
      <text class="subline" x="18" y="55" font-size="19">Chiropractic</text>
      <text class="subline" x="18" y="76" font-size="19">Campaign</text>
      <rect x="190" y="4" width="100" height="84" rx="10" fill="url(#map-fill)" role="img" aria-label="Map of Australia marking Sydney"/>
      <text class="place-label" x="241" y="52" text-anchor="middle" font-size="19">Sydney</text>
      <text class="tagline" x="301" y="53" font-size="21">Chiropractic Campaign</text>
      <polygon class="band" points="605,0 728,0 728,90 536,90"/>
      <rect x="605" y="2" width="100" height="88" fill="url(#figure-fill)" opacity="0.85" role="img" aria-label="Illustration of a spine and skeleton, back view, hand on neck"/>
    </svg>
  </div>

</main>
</body>
</html>
```